velto renovation roof

We need a flyer for a new york based company called velto renovations. We are looking to promote our roofing/window/siding/concrete service.

We are a construction company with over 30 years in the business, but have set up a new company to specialize in roofing - windows - siding. We do offer general renovation service both interior (tiles, paint , Sheetrock, etc) as well as concrete work (driveways, sidewalk) but we think it may be to much information for the flyer. We are fully insured and licensed

We are open to all ideas (I will include a picture of a design that caught our eye from your site).

Target Market(s)

home owners, building managers in the tri state area. We are a New York based company

Industry/Entity Type

Construction

```html
<!DOCTYPE html>
<html lang="en">
<head>
<meta charset="utf-8">
<title>velto renovations – flyers</title>
<link rel="stylesheet" href="https://fonts.googleapis.com/css2?family=Source+Sans+3:wght@400;600;700&display=swap">
<style>
  :root {
    --stage: #5a5a5a;
    --sky-deep: #9fd6ef;
    --sky-light: #e2f3fb;
    --brand-blue: #2b3595;
    --navy-band: #232463;
    --ink-grey: #4a4a4a;
    --ink-dark: #2a2a2a;
    --white: #ffffff;
  }
  * { box-sizing: border-box; margin: 0; padding: 0; }
  html, body {
    width: 1200px; height: 1151px; overflow: hidden;
    background: var(--stage);
    font-family: "Source Sans 3", "Myriad Pro", sans-serif;
  }
  .flyer {
    position: absolute;
    background: var(--white);
    box-shadow: 4px 6px 10px rgba(0,0,0,0.45);
    overflow: hidden;
  }
  .flyer--strip { left: 47px; top: 64px; width: 1010px; height: 476px; }
  .flyer--feature { left: 93px; top: 602px; width: 1012px; height: 474px; }

  .headline-area {
    position: absolute; left: 0; top: 0; width: 100%; height: 182px;
    background: linear-gradient(90deg, var(--sky-deep) 0%, var(--sky-light) 45%, var(--sky-light) 60%, var(--sky-deep) 100%);
  }
  .headline {
    position: absolute; left: 33px; top: 20px;
    color: var(--ink-grey); font-size: 34px; line-height: 47px; font-weight: 400;
  }
  .headline__shout { text-transform: uppercase; }

  .brand {
    position: absolute; display: flex; align-items: center; gap: 22px;
    color: var(--brand-blue); font-weight: 600;
  }
  .brand__name { display: flex; flex-direction: column; line-height: 1; }
  .brand__top { font-size: 50px; letter-spacing: 9px; text-transform: uppercase; }
  .brand__bottom { font-size: 37px; margin-top: 2px; }
  .brand__mark { width: 72px; height: 72px; background: var(--brand-blue); }
  .flyer--strip .brand { left: 628px; top: 50px; }
  .flyer--feature .brand { left: 46px; top: 52px; }

  .photo-row { position: absolute; left: 0; top: 182px; width: 100%; height: 224px; display: flex; gap: 5px; background: var(--white); }
  .photo { height: 100%; }
  .photo--house-wide { width: 357px; background: linear-gradient(180deg, #b9d8ee 0%, #8ea0a0 40%, #b49577 70%, #4f6a3c 100%); }
  .photo--roofer { width: 182px; background: linear-gradient(180deg, #a9c3d8 0%, #8c8f8e 35%, #6e6e6c 100%); }
  .photo--window-fitters { width: 227px; background: linear-gradient(90deg, #d6b3a4 0%, #6f8a5a 50%, #c9a393 100%); }
  .photo--siding-crew { flex: 1; background: linear-gradient(90deg, #e9ecef 0%, #a08466 45%, #dfe3e6 100%); }

  .service-band {
    position: absolute; left: 0; bottom: 0; width: 100%; height: 70px;
    background: var(--navy-band); color: var(--white);
    display: flex; align-items: center; justify-content: space-between;
  }
  .flyer--strip .service-band { padding: 0 18px 0 22px; }
  .flyer--feature .service-band { padding: 0 21px 0 22px; }
  .service-band__list { font-size: 19px; font-weight: 400; }
  .service-band__call { font-size: 26px; font-weight: 700; }

  .feature-panel {
    position: absolute; left: 0; top: 0; width: 426px; height: 404px;
    background: linear-gradient(90deg, var(--sky-deep) 0%, var(--sky-light) 100%);
  }
  .offer { position: absolute; left: 0; width: 420px; text-align: center; }
  .offer__title { top: 213px; font-size: 34px; color: var(--ink-grey); font-weight: 400; text-transform: uppercase; }
  .offer__note { top: 270px; font-size: 25px; color: var(--ink-dark); }
  .offer__web { top: 352px; font-size: 22px; color: var(--brand-blue); font-weight: 600; }
  .photo--house-feature {
    position: absolute; left: 426px; top: 0; width: 586px; height: 404px;
    background: linear-gradient(180deg, #7fb3e2 0%, #b8d6ee 30%, #7e8f86 52%, #c7a884 72%, #5d7a43 100%);
  }
</style>
</head>
<body>

<section class="flyer flyer--strip">
  <div class="headline-area">
    <p class="headline">you get comlete service from<br>start to finish. Just call &amp; tell us...<br><span class="headline__shout">What you want...!</span></p>
    <div class="brand">
      <div class="brand__name"><span class="brand__top">velto</span><span class="brand__bottom">renovations</span></div>
      <span class="brand__mark"></span>
    </div>
  </div>
  <div class="photo-row">
    <div class="photo photo--house-wide" role="img" aria-label="Photo of a stone and stucco house with a new shingle roof"></div>
    <div class="photo photo--roofer" role="img" aria-label="Photo of a roofer laying shingles"></div>
    <div class="photo photo--window-fitters" role="img" aria-label="Photo of two workers installing a window frame"></div>
    <div class="photo photo--siding-crew" role="img" aria-label="Photo of workers on ladders installing siding"></div>
  </div>
  <div class="service-band">
    <span class="service-band__list">Roofing | Window | Siding | General Renovation Service In The New York Area</span>
    <span class="service-band__call">Call: 555-013-4782</span>
  </div>
</section>

<section class="flyer flyer--feature">
  <div class="feature-panel">
    <div class="brand">
      <div class="brand__name"><span class="brand__top">velto</span><span class="brand__bottom">renovations</span></div>
      <span class="brand__mark"></span>
    </div>
    <p class="offer offer__title">Free Estimates</p>
    <p class="offer offer__note">Fully licensed &amp; insured</p>
    <p class="offer offer__web">www.VeltoReno.net</p>
  </div>
  <div class="photo--house-feature" role="img" aria-label="Photo of a large stone and stucco house with a green shingle roof under a blue sky"></div>
  <div class="service-band">
    <span class="service-band__list">Roofing | Window | Siding | General Renovation Service In The New York Area</span>
    <span class="service-band__call">Call: 555-013-4782</span>
  </div>
</section>

</body>
</html>
```